Thank you for shopping with us business card

We would like a thank you card for our rebranded business. We used to be "Brindle Goods" but are now "Marlow Finds. Old thank you card and new logo will be attached for reference. New thank you card does not have to be same design as old thank you card, but please use new logo.
Shopmart URL is now marlowfinds.shopmart.example
Instagram is @Marlow_Finds
Email is marlowfinds@mailbox.example
Thank you!

Contact Information for Business Card

Shopmart site, email, Instagram

```html
<!DOCTYPE html>
<html lang="en">
<head>
<meta charset="utf-8">
<title>Marlow Finds – Thank You Card</title>
<link rel="stylesheet" href="https://fonts.googleapis.com/css2?family=Bebas+Neue&family=Montserrat:wght@400;600;700&display=swap">
<style>
  :root {
    --page-bg: #e9e6e1;
    --card-black: #1f1f20;
    --card-dark: #2a2a2b;
    --band-grey: #4b4b4d;
    --footer-grey: #353536;
    --emboss: #3b3b3d;
    --ink-white: #ffffff;
    --ink-soft: #e4e4e4;
  }
  * { margin: 0; padding: 0; box-sizing: border-box; }
  html, body { width: 1200px; height: 913px; overflow: hidden; }
  body {
    background: var(--page-bg);
    display: flex;
    align-items: center;
    justify-content: center;
    gap: 40px;
    font-family: "Montserrat", Arial, sans-serif;
  }
  .card {
    width: 540px;
    height: 309px;
    border-radius: 4px;
    position: relative;
    overflow: hidden;
    box-shadow: 0 6px 18px rgba(0,0,0,0.25);
  }

  /* Front */
  .card-front {
    background: var(--card-black);
    display: flex;
    align-items: center;
    justify-content: center;
    gap: 14px;
  }
  .brand-mark {
    width: 22px; height: 22px;
    border-radius: 50%;
    background: var(--emboss);
  }
  .brand-name {
    font-family: "Montserrat", Arial, sans-serif;
    font-weight: 700;
    font-size: 34px;
    letter-spacing: 1px;
    text-transform: uppercase;
    color: var(--emboss);
  }

  /* Back */
  .card-back { background: var(--card-dark); }
  .headline {
    position: absolute;
    left: 0; right: 0; top: 42px;
    text-align: center;
    font-family: "Bebas Neue", Impact, sans-serif;
    font-weight: 400;
    color: var(--ink-white);
    line-height: 0.9;
  }
  .headline-main { display: block; font-size: 68px; letter-spacing: 1px; }
  .headline-sub { display: block; font-size: 44px; letter-spacing: 1px; }
  .message-band {
    position: absolute;
    left: 0; right: 0; top: 162px;
    height: 78px;
    background: var(--band-grey);
    display: flex;
    align-items: center;
    justify-content: center;
    text-align: center;
    padding: 0 30px;
    font-size: 13px;
    line-height: 1.6;
    color: var(--ink-soft);
  }
  .contact-row {
    position: absolute;
    left: 0; right: 0; bottom: 0;
    height: 69px;
    background: var(--footer-grey);
    display: flex;
    align-items: center;
    justify-content: space-between;
    gap: 12px;
    padding: 0 18px;
    font-size: 10px;
    color: var(--ink-white);
  }
  .contact-item { display: flex; align-items: center; gap: 6px; white-space: nowrap; }
  .contact-icon {
    flex: none;
    width: 16px; height: 16px;
    border-radius: 50%;
    background: var(--ink-white);
    display: flex; align-items: center; justify-content: center;
  }
  .contact-icon svg { width: 10px; height: 10px; }
</style>
</head>
<body>
  <section class="card card-front" aria-label="Card front">
    <span class="brand-mark"></span>
    <span class="brand-name">Marlow Finds</span>
  </section>

  <section class="card card-back" aria-label="Card back">
    <h1 class="headline">
      <span class="headline-main">Thank You</span>
      <span class="headline-sub">For Purchase</span>
    </h1>
    <p class="message-band">Your purchase made my day and I hope this package brighten yours.<br>Please come back and leave a review!</p>
    <div class="contact-row">
      <span class="contact-item">
        <span class="contact-icon">
          <svg viewBox="0 0 10 10"><rect x="1" y="2.5" width="8" height="5.5" fill="none" stroke="#353536" stroke-width="1"/><polyline points="1,2.5 5,5.5 9,2.5" fill="none" stroke="#353536" stroke-width="1"/></svg>
        </span>
        marlowfinds@mailbox.example
      </span>
      <span class="contact-item">
        <span class="contact-icon">
          <svg viewBox="0 0 10 10"><circle cx="5" cy="5" r="3.8" fill="none" stroke="#353536" stroke-width="1"/><line x1="1.2" y1="5" x2="8.8" y2="5" stroke="#353536" stroke-width="0.8"/><ellipse cx="5" cy="5" rx="1.6" ry="3.8" fill="none" stroke="#353536" stroke-width="0.8"/></svg>
        </span>
        marlowfinds.shopmart.example
      </span>
      <span class="contact-item">
        <span class="contact-icon"></span>
        @Marlow_Finds
      </span>
    </div>
  </section>
</body>
</html>
```